Bref créative
Business card and stationary design for home inspector
Keystone Ridge Home Inspection LLC
Professional
Walter Brunow
Owner/Founder
287 Fenwick Lane
Mooresville, NC 28942
walt@KeystoneRidgeHomeInspection.example
www.KeystoneRidgeHomeInspection.example
NC Home Inspector lic #6817
NC General Contractor lic # 58093
i would like to see both single and double sided business cards.... im not sure which i want yet... if you submit double sided maybe have my logo on the backside....

```html
<!DOCTYPE html>
<html lang="en">
<head>
<meta charset="utf-8">
<title>Keystone Ridge Home Inspection – Stationery</title>
<link href="https://fonts.googleapis.com/css2?family=Open+Sans:wght@400;700;800&display=swap" rel="stylesheet">
<style>
:root{
  --bg:#ebecee;
  --paper:#ffffff;
  --navy:#0c2a66;
  --blue:#1f5fb8;
  --sky:#5fa2e6;
  --ink:#2c3440;
  --muted:#8a929c;
  --faint:#e6ebf2;
  --shadow:0 2px 5px rgba(0,0,0,.18);
}
*{box-sizing:border-box;margin:0;padding:0}
html,body{width:1200px;height:456px;overflow:hidden;background:var(--bg);font-family:"Open Sans",Arial,sans-serif;color:var(--ink)}
.canvas{position:relative;width:1200px;height:456px}
.sheet{position:absolute;background:var(--paper);box-shadow:var(--shadow);overflow:hidden}
.wave{position:absolute;left:0;width:100%}
.brand{display:flex;align-items:center;gap:4px}
.brand-dot{width:14px;height:14px;border-radius:50%;background:var(--blue);flex:none}
.brand-name{font-weight:800;color:var(--navy);font-size:5px;line-height:1.15;text-transform:uppercase;max-width:60px}
.faint-mark{position:absolute;border-radius:50%;border:10px solid var(--faint)}
.tiny{font-size:3.2px;color:var(--muted);line-height:1.5}

/* business cards */
.card-front{left:48px;top:190px;width:168px;height:80px}
.card-front .brand{position:absolute;left:10px;top:18px}
.card-front .brand-dot{width:20px;height:20px}
.card-front .brand-name{font-size:5.5px;max-width:70px}
.card-front .contact{position:absolute;left:92px;top:16px}
.card-front .contact b{display:block;font-size:4.5px;color:var(--navy)}
.card-back{left:48px;top:278px;width:168px;height:80px;background:linear-gradient(135deg,var(--navy),var(--blue))}
.card-back .faint-mark{left:-14px;top:-4px;width:80px;height:80px;border-color:rgba(255,255,255,.12)}
.card-back .brand{position:absolute;left:12px;top:30px}
.card-back .brand-dot{background:var(--sky)}
.card-back .brand-name{color:#fff;font-size:5.5px;max-width:80px}

/* letterhead & fax */
.letterhead{left:233px;top:36px;width:212px;height:386px}
.fax{left:461px;top:36px;width:224px;height:386px}
.sheet .top-brand{position:absolute;left:40px;top:14px}
.sheet .addr{position:absolute;left:92px;top:16px}
.sheet .faint-mark.big{left:50%;top:52%;width:130px;height:130px;margin:-65px 0 0 -65px;border-width:14px}
.foot{position:absolute;right:12px;bottom:6px;text-align:right;color:#fff}
.fax-title{position:absolute;right:22px;top:60px;font-size:11px;font-weight:700;color:var(--ink)}
.fax-form{position:absolute;left:22px;right:22px;top:80px;display:grid;grid-template-columns:1fr 1fr;column-gap:10px;row-gap:5px;font-size:4px;color:var(--ink)}
.fax-form span{border-bottom:.5px solid #c4c9d0;padding-bottom:1px}
.fax-checks{position:absolute;left:22px;right:22px;top:128px;display:flex;justify-content:space-between;font-size:3.4px;color:var(--ink)}
.fax-checks i{display:inline-block;width:3px;height:3px;border:.5px solid var(--ink);margin-right:1px;vertical-align:middle}

/* envelopes */
.env{position:absolute;background:var(--paper);box-shadow:var(--shadow)}
.env-back{left:710px;top:43px;width:294px;height:160px}
.env-back svg{position:absolute;inset:0}
.env-back .flap-dot{position:absolute;left:141px;top:84px;width:14px;height:14px;border-radius:50%;background:var(--blue)}
.env-blue{left:842px;top:168px;width:330px;height:150px;overflow:hidden}
.env-blue svg{position:absolute;inset:0}
.env-blue .flap-dot{position:absolute;left:157px;top:70px;width:16px;height:16px;border-radius:50%;background:#fff;border:3px solid var(--sky)}
.env-front{left:710px;top:228px;width:294px;height:158px;overflow:hidden}
.env-front .return{position:absolute;left:8px;top:118px}
.env-front .addr-to{position:absolute;left:150px;top:70px;font-size:4px;color:var(--ink);line-height:1.5}
</style>
</head>
<body>
<main class="canvas">

  <!-- business card: front -->
  <section class="sheet card-front">
    <div class="brand"><span class="brand-dot"></span><span class="brand-name">Keystone Ridge Home Inspection</span></div>
    <div class="contact tiny">
      <b>Walter Brunow</b>Owner/Founder<br>287 Fenwick Lane<br>Mooresville, NC 28942<br>walt@KeystoneRidgeHomeInspection.example<br>NC Home Inspector lic #6817
    </div>
    <svg class="wave" style="bottom:0" width="168" height="22" viewBox="0 0 168 22" preserveAspectRatio="none">
      <path d="M0 14 Q60 2 168 10 L168 22 L0 22Z" fill="var(--sky)"/>
      <path d="M0 17 Q70 8 168 14 L168 22 L0 22Z" fill="var(--navy)"/>
    </svg>
  </section>

  <!-- business card: back -->
  <section class="sheet card-back">
    <span class="faint-mark"></span>
    <div class="brand"><span class="brand-dot"></span><span class="brand-name">Keystone Ridge Home Inspection LLC</span></div>
  </section>

  <!-- letterhead -->
  <section class="sheet letterhead">
    <div class="brand top-brand"><span class="brand-dot"></span><span class="brand-name">Keystone Ridge Home Inspection</span></div>
    <div class="addr tiny">287 Fenwick Lane<br>Mooresville, NC 28942</div>
    <span class="faint-mark big"></span>
    <svg class="wave" style="bottom:0" width="212" height="40" viewBox="0 0 212 40" preserveAspectRatio="none">
      <path d="M0 20 Q90 0 212 14 L212 40 L0 40Z" fill="var(--sky)"/>
      <path d="M0 26 Q100 8 212 20 L212 40 L0 40Z" fill="var(--navy)"/>
    </svg>
    <div class="foot tiny" style="color:#fff">www.KeystoneRidgeHomeInspection.example</div>
  </section>

  <!-- fax sheet -->
  <section class="sheet fax">
    <div class="brand top-brand"><span class="brand-dot"></span><span class="brand-name">Keystone Ridge Home Inspection</span></div>
    <div class="addr tiny">287 Fenwick Lane<br>Mooresville, NC 28942</div>
    <div class="fax-title">FAX</div>
    <div class="fax-form">
      <span>To:</span><span>From:</span>
      <span>Fax:</span><span>Pages:</span>
      <span>Phone:</span><span>Date:</span>
      <span>Re:</span><span>CC:</span>
    </div>
    <div class="fax-checks">
      <span><i></i>Urgent</span><span><i></i>For review</span><span><i></i>Please comment</span><span><i></i>Please reply</span><span><i></i>Please recycle</span>
    </div>
    <span class="faint-mark big"></span>
    <svg class="wave" style="bottom:0" width="224" height="40" viewBox="0 0 224 40" preserveAspectRatio="none">
      <path d="M0 20 Q90 0 224 14 L224 40 L0 40Z" fill="var(--sky)"/>
      <path d="M0 26 Q100 8 224 20 L224 40 L0 40Z" fill="var(--navy)"/>
    </svg>
    <div class="foot tiny">www.KeystoneRidgeHomeInspection.example</div>
  </section>

  <!-- envelope: back, white flap -->
  <section class="env env-back">
    <svg width="294" height="160" viewBox="0 0 294 160">
      <path d="M0 0 L147 92 L294 0" fill="none" stroke="#d5d9df" stroke-width="1"/>
      <path d="M0 160 L120 80 M294 160 L174 80" stroke="#eceef1" stroke-width="1"/>
    </svg>
    <span class="flap-dot"></span>
  </section>

  <!-- envelope: back, blue flap -->
  <section class="env env-blue">
    <svg width="330" height="150" viewBox="0 0 330 150">
      <defs><linearGradient id="flap" x1="0" y1="0" x2="0" y2="1"><stop offset="0" stop-color="var(--navy)"/><stop offset="1" stop-color="var(--blue)"/></linearGradient></defs>
      <path d="M0 0 L330 0 L165 85Z" fill="url(#flap)"/>
    </svg>
    <span class="flap-dot"></span>
  </section>

  <!-- envelope: front -->
  <section class="env env-front">
    <div class="brand" style="position:absolute;left:10px;top:10px"><span class="brand-dot"></span><span class="brand-name">Keystone Ridge Home Inspection</span></div>
    <div class="return tiny">287 Fenwick Lane<br>Mooresville, NC 28942</div>
    <svg class="wave" style="bottom:0" width="294" height="24" viewBox="0 0 294 24" preserveAspectRatio="none">
      <path d="M0 14 Q140 0 294 10 L294 24 L0 24Z" fill="var(--sky)"/>
      <path d="M0 18 Q150 6 294 15 L294 24 L0 24Z" fill="var(--navy)"/>
    </svg>
  </section>

</main>
</body>
</html>
```